Can art for new pre workout drink

Can Design for Dorvu Fuel – Non-Stimulant Performance Drink

Background:
Dorvu Fuel is a non-stimulant performance and focus pre workout drink. It’s designed for gym-goers and night-time users who want clean energy and focus without caffeine . Our formula is optimized for physical performance, mental clarity, and hydration – without relying on stimulants.

We are launching our first flavor: “Original”, and we need a bold, modern, and professional can design to reflect our unique positioning in the fitness and nootropic space.

Design Goals:

Clean, minimalistic, and modern look

Emphasize that it’s non-stimulant

Should feel premium and appeal to gym/fitness lovers

Needs to stand out on shelves and social media ads

Should balance scientific and cool (think more Hollow Crane meets clean supplement brand)

Design Elements Required:

Logo: Use our existing “Dorvu Fuel” logo (I’ll upload it) – do not change the font

Flavor Name: “Original”

optional - Callouts/Claims (place in a clean way, maybe near the bottom or side):

“Non-Stimulant Performance Blend”

“Boost Focus • Support Performance • Enhance Hydration”

Can Size: 12 fl oz (355ml)

Leave space for: Nutrition label, barcode, ingredients (we’ll add these later)

Colors:

Main brand colors: Black & White but feel free to branch out

Accent colors are optional – feel free to propose subtle color highlights to add energy or represent the flavor if needed. Avoid neons.

Inspiration:

Clean energy drink designs (e.g., Tusk, Varnok, Mirelo Energy, Hollow Crane)

Supplement brands like Brava, Quillstone Works, or Pardi Brew

What to Avoid:

Overly “extreme” or loud energy drink styles

Caffeine references

Cheap, overused stock imagery or messy clutter

Deliverables:

Full-color can mockup (front and side views)

Editable design file (AI or PSD)

Print-ready PDF with bleed

Fonts used (available for commercial use not just personal)

Target Market(s)

18-30 Male and female

Industry/Entity Type

Energy drink

Requirements
Must have
• label

```html
<!DOCTYPE html>
<html lang="en">
<head>
<meta charset="utf-8">
<title>Dorvu Fuel – Original Can Label</title>
<link rel="stylesheet" href="https://fonts.googleapis.com/css2?family=Archivo+Black&family=Roboto+Condensed:wght@400;600&display=swap">
<style>
  :root {
    --bg-top: #3a3a3a;
    --bg-bottom: #8e8e8e;
    --label-black: #0c0c0c;
    --ink-white: #f4f4f4;
    --ink-soft: #cfcfcf;
    --window-light: #dfe8ea;
    --window-mid: #9fb3b8;
    --window-deep: #4e6166;
  }
  * { box-sizing: border-box; margin: 0; padding: 0; }
  html, body { width: 1200px; height: 1200px; overflow: hidden; }
  body {
    background: linear-gradient(180deg, var(--bg-top) 0%, var(--bg-bottom) 100%);
    position: relative;
    font-family: "Roboto Condensed", "Arial Narrow", sans-serif;
  }
  .can-label {
    position: absolute;
    left: 455px;
    top: 132px;
    width: 290px;
    height: 936px;
    background: var(--label-black);
    overflow: hidden;
  }
  .tagline-top {
    position: absolute;
    top: 26px;
    left: 0;
    width: 100%;
    text-align: center;
    font-size: 11px;
    letter-spacing: 1px;
    color: var(--ink-soft);
    font-weight: 600;
  }
  .brand-name {
    position: absolute;
    font-family: "Archivo Black", "Arial Black", sans-serif;
    color: var(--ink-white);
    writing-mode: vertical-rl;
    transform: rotate(180deg);
    line-height: 1;
    white-space: nowrap;
  }
  .brand-name--main {
    left: 30px;
    top: 140px;
    font-size: 118px;
  }
  .brand-name--sub {
    left: 168px;
    top: 160px;
    font-size: 34px;
    letter-spacing: 1px;
  }
  .flavor-window {
    position: absolute;
    left: 146px;
    top: 445px;
    width: 144px;
    height: 205px;
    border-radius: 12px 0 0 12px;
    background: linear-gradient(180deg, var(--window-light) 0%, var(--window-mid) 55%, var(--window-deep) 100%);
  }
  .flavor-name {
    position: absolute;
    left: 26px;
    top: 732px;
    font-size: 46px;
    font-weight: 600;
    color: var(--ink-white);
    letter-spacing: -0.5px;
  }
  .claim {
    position: absolute;
    left: 27px;
    top: 808px;
    font-size: 15px;
    line-height: 23px;
    color: var(--ink-white);
    text-transform: uppercase;
  }
  .volume {
    position: absolute;
    left: 27px;
    top: 868px;
    font-size: 14px;
    color: var(--ink-white);
    text-transform: uppercase;
  }
</style>
</head>
<body>
  <main class="can-label">
    <p class="tagline-top">FEEL THE DORVU DIFFERENCE</p>
    <h1>
      <span class="brand-name brand-name--main">Dorvu</span>
      <span class="brand-name brand-name--sub">FUEL</span>
    </h1>
    <div class="flavor-window" role="img" aria-label="Close-up of clear sparkling liquid with rising bubbles"></div>
    <p class="flavor-name">Original</p>
    <p class="claim">Non-Stimulant<br>Performance Blend</p>
    <p class="volume">12 fl oz</p>
  </main>
</body>
</html>
```